Design logo, business cards, and web page for new web and bi development consulting company

I've started a Web and Business Intelligence development consulting company. We develop on Bramquist's stack, Visual Sudio and SQL Server. We develop responsive web sites and business intelligence platforms. I plan on focusing on small to medium sized business as my client base. I need a logo, business cards, and a one page web site. We will do more with the web site with you in the next six months if the business survives. The name of the company is Korvale Integration Solutions, Korvale for short.

Target Market(s)

small to medium sized businesses

Industry/Entity Type

Business

Contact Information for Business Card

logo
name
title
email
phone

Logo Text

Korvale Integration Solutions - web and data solutions

Coding

Coded - Design and coding required

Number of Pages Required

1 page

Font styles to use
Sans Serif

Colors
0355a3
0092cd
00a88f
6b449b

Requirements
Nice to have
• web and data solutions

```html
<!DOCTYPE html>
<html lang="en">
<head>
<meta charset="utf-8">
<title>Korvale Integration Solutions – Business Cards</title>
<link rel="stylesheet" href="https://fonts.googleapis.com/css2?family=Source+Sans+3:wght@400&display=swap">
<style>
  :root {
    --purple: #6b449b;
    --blue: #1292ce;
    --white: #ffffff;
    --backdrop: #f3f3f3;
    --text-font: "Source Sans 3", sans-serif;
  }
  * { box-sizing: border-box; margin: 0; padding: 0; }
  html, body {
    width: 1200px;
    height: 1000px;
    overflow: hidden;
  }
  body {
    position: relative;
    background: var(--backdrop);
    font-family: var(--text-font);
    font-weight: 400;
    color: var(--white);
  }
  .card {
    position: absolute;
    width: 625px;
    height: 357px;
    overflow: hidden;
  }
  .card-back {
    left: 100px;
    top: 150px;
    background: var(--purple);
  }
  .card-front {
    left: 499px;
    top: 493px;
    background: var(--blue);
  }
  .card-band {
    position: absolute;
    bottom: 0;
  }
  .card-back .card-band { left: 0; }
  .card-front .card-band { right: 0; }

  .brand {
    position: absolute;
    display: flex;
    align-items: center;
    gap: 16px;
  }
  .brand-dot {
    width: 70px;
    height: 70px;
    border-radius: 50%;
    background: var(--white);
    flex: none;
  }
  .brand-text { line-height: 1; color: var(--white); }
  .brand-name {
    display: block;
    font-size: 50px;
    letter-spacing: 0.5px;
  }
  .brand-tagline {
    display: block;
    margin-top: 6px;
    font-size: 12.5px;
    letter-spacing: 2.4px;
    text-transform: uppercase;
  }
  .card-back .brand { left: 300px; top: 140px; }
  .card-front .brand { left: 30px; top: 26px; }

  .contact {
    position: absolute;
    left: 47px;
    top: 175px;
  }
  .contact-name {
    font-size: 23px;
    margin-bottom: 32px;
  }
  .contact-lines {
    list-style: none;
    font-size: 19px;
    line-height: 26px;
  }
</style>
</head>
<body>

  <section class="card card-back" aria-label="Business card, back side">
    <svg class="card-band" width="320" height="24" viewBox="0 0 320 24" aria-hidden="true">
      <polygon points="0,8 290,0 320,12 320,24 0,24" fill="var(--blue)"/>
    </svg>
    <div class="brand">
      <span class="brand-dot"></span>
      <span class="brand-text">
        <span class="brand-name">Korvale</span>
        <span class="brand-tagline">Integration Solutions</span>
      </span>
    </div>
  </section>

  <section class="card card-front" aria-label="Business card, front side">
    <div class="brand">
      <span class="brand-dot"></span>
      <span class="brand-text">
        <span class="brand-name">Korvale</span>
        <span class="brand-tagline">Integration Solutions</span>
      </span>
    </div>
    <div class="contact">
      <p class="contact-name">Daniel Hartwell</p>
      <ul class="contact-lines">
        <li>415 555 0182</li>
        <li>daniel@korvale.com</li>
        <li>www.korvale.com</li>
      </ul>
    </div>
    <svg class="card-band" width="320" height="19" viewBox="0 0 320 19" aria-hidden="true">
      <polygon points="0,0 320,0 320,19 18,19" fill="var(--purple)"/>
    </svg>
  </section>

</body>
</html>
```